We are looking for a 2-page (front and back) 3.67" x 8.5" rack card. . Please refer back to our other Rack Cards for a similar look and feel to the card. This one is titled: Myths and Truths About Memory Loss
The document is for older readers. Do not put text over graphics and keep it simple and easy to read with high contrast.
We want some very simple design element(s) incorporated that convey Native American communities or heritage. But NO headdress, teepee graphics, owls etc. I have included some graphics, please use your creative discretion to use which ones look good on the cards. Please remember to include the funding statement - it can be in a very small font 6/7 point. For more information about our project, please visit https://orvelmesa.net/mind-care/library - This rack card is supported by the Bureau for Wellness Tracking and Outreach (BWT) of the Federal Office of Family and Care Affairs (FOF) as part of a financial assistance award totaling $1,248,702.15 with 100 percent funded by BWT/FOF. The contents are those of the author(s) and do not necessarily represent the official views of, nor an endorsement, by BWT/FOF, or the Federal Administration.
Please feel free to choose one of each of the 2 logos that looks best. We have the QT7 logo and the Mind Wellness Support Hub logo we would like to add. I have added the document and there are images to choose from to use in the rack card. We definitely want to incorporate the coyote in this rack card since it is culturally significant.

```html
<!DOCTYPE html>
<html lang="en">
<head>
<meta charset="utf-8">
<title>About Memory Loss – Myths and Truths Rack Card</title>
<link rel="stylesheet" href="https://fonts.googleapis.com/css2?family=Arimo:ital,wght@0,400;0,700;1,400&display=swap">
<style>
  :root{
    --page:#ffffff;
    --canvas:#ffffff;
    --ink:#231f20;
    --heading:#3a1d1a;
    --teal:#2b8c8c;
    --label:#5b1f1b;
    --rust:#b0483a;
    --band:#a34a3c;
    --row:#e7e7e7;
    --box:#e9e9e9;
    --rule:#9a9a9a;
  }
  *{box-sizing:border-box;margin:0;padding:0}
  html,body{width:1200px;height:1198px;overflow:hidden;background:var(--canvas)}
  body{position:relative;font-family:"Arimo",Arial,sans-serif;color:var(--ink)}

  .rack-card{position:absolute;width:442px;height:1022px;background:var(--page);
    box-shadow:0 2px 8px rgba(0,0,0,.22);overflow:hidden}
  .rack-card--front{left:148px;top:95px}
  .rack-card--back{left:618px;top:84px}

  .hero__photo{position:absolute;left:0;width:245px;height:250px;
    background:linear-gradient(135deg,#e6e1d9 0%,#c2bab0 45%,#948b80 100%)}
  .rack-card--front .hero__photo{top:47px}
  .rack-card--back .hero__photo{top:10px;width:232px;height:246px;
    background:linear-gradient(160deg,#c9b899 0%,#a88f6a 40%,#6f6552 75%,#8b7a5e 100%)}

  .brand{position:absolute;left:325px;width:112px}
  .rack-card--front .brand{top:22px}
  .rack-card--back .brand{top:12px}
  .brand__mark{display:flex;align-items:center;gap:5px;font-weight:700;font-size:34px;color:var(--teal);line-height:1}
  .brand__dot{width:11px;height:11px;background:var(--rust);border-radius:50%}
  .brand__name{margin-top:8px;font-weight:700;font-size:9px;line-height:1.2;color:var(--rust);text-transform:uppercase}

  .pattern-band{position:absolute;left:0;width:442px;height:13px;background:var(--band)}
  .rack-card--front .pattern-band{top:310px}
  .rack-card--back .pattern-band{top:257px}

  .content{position:absolute;left:22px;right:22px}
  .rack-card--front .content{top:338px}
  .rack-card--back .content{top:285px}

  .title{text-align:center;font-weight:700;line-height:1.05}
  .title__top{display:block;font-size:21px;color:var(--heading)}
  .title__bottom{display:block;font-size:23px;color:var(--teal)}
  .intro{font-size:14.5px;line-height:1.2;margin-top:6px;text-align:justify;text-align-last:center}
  .intro p+p{margin-top:2px}
  .versus{margin:14px 0 8px;text-align:center;font-weight:700;font-size:25px;color:var(--teal)}
  .versus span{color:var(--heading)}

  .myth-list{font-size:13.5px;line-height:1.22}
  .pair+.pair{margin-top:12px}
  .pair__row{display:grid;grid-template-columns:52px 1fr;padding:3px 6px}
  .pair__row--myth{background:var(--row);color:var(--ink)}
  .pair__row--truth{color:var(--teal)}
  .pair__label{font-weight:700;color:var(--label)}

  .dots{display:flex;justify-content:center;gap:4px;margin:12px 0}
  .dots i{width:3px;height:3px;border-radius:50%;background:var(--rust)}

  .quote{position:relative;border:1px solid var(--rule);padding:14px 30px 12px;margin:0 8px}
  .quote__text{font-weight:700;font-size:15px;line-height:1.3;text-align:center}
  .quote__cite{display:block;margin-top:10px;text-align:right;padding-right:10px;font-style:italic;font-size:13px;line-height:1.25}
  .quote__mark{position:absolute;font-size:30px;font-weight:700;line-height:1}
  .quote__mark--open{left:10px;top:10px}
  .quote__mark--close{right:10px;bottom:2px}

  .site{position:absolute;left:0;right:0;text-align:center;font-weight:700;font-size:15px}
  .rack-card--front .site{top:990px}
  .rack-card--back .site{top:906px}

  .subhead{text-align:center;font-weight:700;font-size:15px;margin-bottom:8px}
  .action{background:var(--box);border-radius:12px;padding:10px 14px;font-size:14px;line-height:1.25;text-align:justify;text-align-last:center}
  .action p+p{margin-top:2px}

  .partner{display:flex;justify-content:center;align-items:center;gap:6px;margin:12px 0;font-weight:700;font-size:11px;color:var(--rust)}
  .partner__dot{width:20px;height:20px;border-radius:50%;background:var(--rust)}

  .resources{border:1px solid var(--rule);padding:10px 14px;text-align:center}
  .resources__title{font-weight:700;font-size:13.5px;margin-bottom:4px}
  .resource{margin-top:6px}
  .resource__name{font-weight:700;font-size:11px}
  .resource__url{display:block;background:var(--box);font-size:9.5px;padding:2px 4px;margin-top:2px;word-break:break-all}

  .funding{position:absolute;left:40px;right:40px;top:945px;font-size:7.5px;line-height:1.3;text-align:center}
</style>
</head>
<body>

<article class="rack-card rack-card--front">
  <div class="hero__photo" role="img" aria-label="Photograph of a Native Elder seated against a wall, wearing a white blouse and patterned skirt"></div>
  <div class="brand">
    <div class="brand__mark"><span class="brand__dot"></span>QT7</div>
    <div class="brand__name">Northern Circle for Elder Wellbeing</div>
  </div>
  <div class="pattern-band" role="img" aria-label="Native geometric pattern band in rust and cream"></div>

  <section class="content">
    <h1 class="title"><span class="title__top">ABOUT MEMORY LOSS</span><span class="title__bottom">MYTHS AND TRUTHS</span></h1>
    <div class="intro">
      <p>People sometimes believe things about memory loss that are not true. Misunderstandings can make it harder for Elders in Native communities to get the help they need when they start having memory issues.</p>
      <p>Below are some common myths and truths about memory loss, Alzheimer’s disease, and related dementias.</p>
    </div>
    <h2 class="versus">MYTHS <span>VS</span> TRUTH</h2>

    <div class="myth-list">
      <div class="pair">
        <div class="pair__row pair__row--myth"><span class="pair__label">Myth:</span><span>Getting Alzheimer’s is a normal part of aging.</span></div>
        <div class="pair__row pair__row--truth"><span class="pair__label">Truth:</span><span>It is a disease that not everyone will get.</span></div>
      </div>
      <div class="pair">
        <div class="pair__row pair__row--myth"><span class="pair__label">Myth:</span><span>Memory problems and forgetfulness are definite signs of dementia.</span></div>
        <div class="pair__row pair__row--truth"><span class="pair__label">Truth:</span><span>Memory problems do not solely determine<br>if they are dementia.<br>Other medical conditions can cause memory problems.<br>Talk to your doctor.</span></div>
      </div>
      <div class="pair">
        <div class="pair__row pair__row--myth"><span class="pair__label">Myth:</span><span>Only older people can get Alzheimer’s disease.</span></div>
        <div class="pair__row pair__row--truth"><span class="pair__label">Truth:</span><span>There have been cases for people as young as twenty-five, though it is rare to undergo treatment.</span></div>
      </div>
    </div>

    <div class="dots"><i></i><i></i><i></i><i></i><i></i><i></i><i></i><i></i></div>

    <blockquote class="quote">
      <span class="quote__mark quote__mark--open">“</span>
      <p class="quote__text">The beauty in life is each day is a new day to try again and be a better version of myself than yesterday.</p>
      <cite class="quote__cite">Lena Sorrel (Stonecreek Nation),<br>personal communication with the author.</cite>
      <span class="quote__mark quote__mark--close">”</span>
    </blockquote>
  </section>

  <footer class="site">www.orvelmesa.net</footer>
</article>

<article class="rack-card rack-card--back">
  <div class="hero__photo" role="img" aria-label="Photograph of a coyote walking through dry golden grass"></div>
  <div class="brand">
    <div class="brand__mark"><span class="brand__dot"></span>QT7</div>
    <div class="brand__name">Northern Circle for Elder Wellbeing</div>
  </div>
  <div class="pattern-band" role="img" aria-label="Native geometric pattern band in rust and cream"></div>

  <section class="content">
    <div class="myth-list">
      <div class="pair">
        <div class="pair__row pair__row--myth"><span class="pair__label">Myth:</span><span>People with Alzheimer’s disease cannot be happy.</span></div>
        <div class="pair__row pair__row--truth"><span class="pair__label">Truth:</span><span>A person with memory loss can experience strong moods and emotions but still enjoy life and relationships.</span></div>
      </div>
      <div class="pair">
        <div class="pair__row pair__row--myth"><span class="pair__label">Myth:</span><span>Dementia can be prevented by a certain supplement or food.</span></div>
        <div class="pair__row pair__row--truth"><span class="pair__label">Truth:</span><span>Healthy eating may help overall wellness, including brain health. No additional supplements will completely prevent the onset of dementia.</span></div>
      </div>
      <div class="pair">
        <div class="pair__row pair__row--myth"><span class="pair__label">Myth:</span><span>Alzheimer’s is reversible through prescription drugs.</span></div>
        <div class="pair__row pair__row--truth"><span class="pair__label">Truth:</span><span>There are prescription drugs to address symptoms of Alzheimer’s and dementia, but there are no medicines that can reverse them.</span></div>
      </div>
    </div>

    <div class="dots"><i></i><i></i><i></i><i></i><i></i><i></i><i></i><i></i></div>

    <h2 class="subhead">What You Can Do</h2>
    <div class="action">
      <p>If you or someone you love is having memory problems, do not wait. Talk to a healthy provider you trust.</p>
      <p>Learning the truth can help keep our Elders strong and supported.</p>
    </div>

    <div class="partner"><span class="partner__dot"></span>Mind Wellness Support Hub</div>

    <aside class="resources">
      <h3 class="resources__title">For More Myth-Busting Information:</h3>
      <div class="resource">
        <div class="resource__name">12 Common Alzheimer’s Disease Myths on Kindred Home Guide:</div>
        <span class="resource__url">https://www.kindredhomeguide.com/memory-myths-busted/</span>
      </div>
      <div class="resource">
        <div class="resource__name">Memory Alliance Network Myths vs. Facts:</div>
        <span class="resource__url">https://www.memoryalliancenet.org/dementia/research/trials/myths-vs-facts</span>
      </div>
      <div class="resource">
        <div class="resource__name">QT7 Brain Health Resources:</div>
        <span class="resource__url">https://orvelmesa.net/mind-care/library</span>
      </div>
    </aside>
  </section>

  <footer class="site">www.orvelmesa.net</footer>
  <p class="funding">This rack card is supported by the Bureau for Wellness Tracking and Outreach (BWT) of the Federal Office of Family and Care Affairs (FOF) as part of a financial assistance award totaling $1,248,702.15 with 100 percent funded by BWT/FOF. The contents are those of the author(s) and do not necessarily represent the official views of, nor an endorsement, by BWT/FOF, or the Federal Administration.</p>
</article>

</body>
</html>
```